Business Card Design Project

Vexolyte will provide 3D analysis of remote sensing digital data sets of airborne (aircraft/UAV) and satellite data in order to deliver 3D geospatial mapping information, videos and augmented reality products. Typical high end customers are military and security related customers, line object infrastructure owners or providers (pipelines gas/oil/fuel/water, energy lines, borders, coastal zones and rivers, transportation roads on the sea, roads, and railway systems). All these potential customers are linked to regular service monitoring, surveillance and reconnaissance covering cities, counties and countries. The company will provide 3D presentation of infrastructure (which is likely to become a binding requirement in Europe and other countries), disaster prevention and monitoring.

Target Market(s)

Target market are US based governmental agencies, such as Bureau of Civic Safeguards, Federal Terrasight bureau, Ministery of Garrison Affairs, Office of Landholdings/Federal Strata Bureau, etc as well as commercial entities like gas, utilities, etc > Primary services will be to provide 3D geospatial mapping to support search & rescue, border control, infrastructure (pipeline, electric wires, etc.) management, agriculture, climate control, etc.

Industry/Entity Type

Business

Contact Information for Business Card

Vincent Renz6 Gristmill RdCedar Knolls, NJ 079271-973-652-8379vrenz.straight4ward@gmail.com

Requirements
Must have
• Business card must have the company logo (provided) - and want to keep with the colors in the logo

```html
<!DOCTYPE html>
<html lang="en">
<head>
<meta charset="utf-8">
<title>Vexolyte – Business Card</title>
<link rel="stylesheet" href="https://fonts.googleapis.com/css2?family=Lato:wght@300;400;700&display=swap">
<style>
  :root {
    --backdrop: #e8e5e0;
    --card: #ffffff;
    --accent-red: #d9444c;
    --brand-teal: #6f95a3;
    --text-dark: #3d3d3d;
    --text-mid: #5a5a5a;
  }
  html, body {
    margin: 0;
    padding: 0;
    width: 1200px;
    height: 1023px;
    overflow: hidden;
    background: var(--backdrop);
    font-family: "Lato", sans-serif;
  }
  .business-card {
    position: absolute;
    left: 150px;
    top: 254px;
    width: 900px;
    height: 514px;
    background: var(--card);
    box-shadow: 0 2px 10px rgba(0,0,0,0.12);
  }
  .brand {
    position: absolute;
    left: 150px;
    top: 92px;
    display: flex;
    align-items: center;
    gap: 18px;
  }
  .brand-square {
    width: 22px;
    height: 22px;
    background: var(--accent-red);
  }
  .brand-name {
    font-weight: 300;
    font-size: 68px;
    letter-spacing: 1px;
    color: var(--brand-teal);
    line-height: 1;
  }
  .person {
    position: absolute;
    left: 230px;
    top: 232px;
  }
  .person-name {
    font-size: 32px;
    font-weight: 400;
    color: var(--accent-red);
    margin: 0;
    line-height: 1.1;
  }
  .person-title {
    font-size: 17px;
    color: var(--text-dark);
    margin: 4px 0 0 4px;
  }
  .address {
    position: absolute;
    left: 230px;
    top: 362px;
    font-size: 18px;
    line-height: 1.5;
    color: var(--text-mid);
    text-align: right;
    width: 210px;
  }
  .divider {
    position: absolute;
    left: 472px;
    top: 340px;
    width: 0;
    height: 112px;
    border-left: 3px dotted var(--accent-red);
  }
  .contact-list {
    position: absolute;
    left: 498px;
    top: 346px;
    margin: 0;
    padding: 0;
    list-style: none;
  }
  .contact-item {
    display: flex;
    align-items: center;
    gap: 12px;
    font-size: 18px;
    color: var(--text-dark);
    margin-bottom: 12px;
  }
  .contact-icon {
    width: 22px;
    height: 22px;
    flex: none;
  }
</style>
</head>
<body>
  <div class="business-card">
    <div class="brand">
      <span class="brand-square"></span>
      <span class="brand-name">Vexolyte</span>
    </div>

    <div class="person">
      <p class="person-name">Harold Brisk</p>
      <p class="person-title">Managing Director</p>
    </div>

    <div class="address">
      41 Pelham Ln<br>
      Maple Hollow, NJ 08314
    </div>

    <div class="divider"></div>

    <ul class="contact-list">
      <li class="contact-item">
        <svg class="contact-icon" viewBox="0 0 22 22" aria-hidden="true">
          <rect width="22" height="22" rx="4" fill="var(--accent-red)"/>
          <path d="M7 5.5c.6-.4 1.3-.2 1.6.4l1 2c.2.5.1 1-.3 1.3l-.8.6c.6 1.3 1.6 2.3 2.9 2.9l.6-.8c.3-.4.9-.5 1.3-.3l2 1c.6.3.8 1 .4 1.6l-.8 1.1c-.5.6-1.3.8-2 .5C9.6 14.6 7.4 12.4 6.2 9.1c-.3-.7-.1-1.5.5-2z" fill="#fff"/>
        </svg>
        <span>1-555-218-4093</span>
      </li>
      <li class="contact-item">
        <svg class="contact-icon" viewBox="0 0 22 22" aria-hidden="true">
          <rect width="22" height="22" rx="4" fill="var(--accent-red)"/>
          <rect x="5" y="7" width="12" height="9" rx="1" fill="none" stroke="#fff" stroke-width="1.5"/>
          <path d="M5.5 7.5l5.5 4.5 5.5-4.5" fill="none" stroke="#fff" stroke-width="1.5"/>
        </svg>
        <span>hbrisk.onpath22@mailcove.example</span>
      </li>
    </ul>
  </div>
</body>
</html>
```